LMT Vexa Website

Would like to have a website created that keeps with the branding of our other company; LMT Vexa Corporation. www.harborledgerco.net

Target Market(s)

Medical providers, accounts receivable management

Industry/Entity Type

Accounts Receivable Management

Number of Pages Required

5+ page

Requirements
Must have
• look similar to www.harborledgerco.net, but will have different logo and domain as it is completely separate company

```html
<!DOCTYPE html>
<html lang="en">
<head>
<meta charset="utf-8">
<title>LMT Vexa</title>
<link href="https://fonts.googleapis.com/css2?family=Inter:wght@400;500;600;700&display=swap" rel="stylesheet">
<style>
:root{
  --brick:#8b4a44;
  --teal:#2f5f58;
  --mint:#7cb9a4;
  --ink:#1f1f1f;
  --body:#444;
  --line:#e3e3e3;
  --footer:#3a3a3c;
  --footer-label:#9a9a9c;
}
*{box-sizing:border-box;margin:0;padding:0}
html,body{width:1200px;height:3991px;overflow:hidden}
body{font-family:"Inter",sans-serif;color:var(--ink);background:#fff;position:relative}
.abs{position:absolute}
a{color:inherit;text-decoration:none}

/* header */
.site-header{position:absolute;top:0;left:0;width:1200px;height:76px;background:#fff}
.brand{left:59px;top:27px;display:flex;align-items:center;gap:8px;font-size:17px;font-weight:600;color:var(--teal)}
.brand .mark{width:14px;height:14px;background:var(--brick)}
.main-nav{left:272px;top:31px;display:flex;gap:18px;font-size:13px;color:#222}
.search{left:920px;top:31px;font-size:13px;display:flex;gap:5px;align-items:center}
.client-login{left:1004px;top:16px;width:138px;height:47px;background:var(--brick);color:#fff;font-size:13px;display:flex;align-items:center;justify-content:center}

/* tabs */
.tab-bar{position:absolute;left:0;width:1200px;height:104px;display:flex}
.tab{flex:1;display:flex;align-items:center;justify-content:center;gap:26px;color:#fff;font-size:19px;font-weight:500;text-align:center;line-height:1.2}
.tab.brick{background:var(--brick)}
.tab.teal{background:var(--teal)}
.tab.mint{background:var(--mint)}

/* hero */
.hero{position:absolute;top:180px;left:0;width:1200px;height:558px;background:linear-gradient(100deg,#2c3a3c 0%,#4b5a57 45%,#6f6a5c 70%,#3a3834 100%)}
.hero h1{position:absolute;left:59px;top:112px;font-size:54px;line-height:1.12;color:#fff;font-weight:700}
.hero p{position:absolute;left:59px;top:248px;width:440px;font-size:17px;line-height:29px;color:#fff;font-weight:500}
.btn{position:relative;z-index:2;display:flex;align-items:center;justify-content:center;background:var(--teal);color:#fff;font-size:15px}
.hero .btn{position:absolute;left:59px;top:354px;width:203px;height:59px}

/* welcome */
.welcome{position:absolute;top:738px;left:0;width:1200px;height:408px;text-align:center}
.welcome h2{position:relative;z-index:2;margin-top:78px;font-size:35px;font-weight:600}
.welcome p{position:relative;z-index:2;width:620px;margin:18px auto 0;font-size:14.5px;line-height:27px;color:var(--body)}
.welcome .btn,.cta .btn{width:186px;height:54px;margin:24px auto 0}
.skyline{position:absolute;z-index:1;left:0;bottom:0;width:1200px;height:130px;background:linear-gradient(to bottom,rgba(255,255,255,0) 0%,#f2f2f2 60%,#e8e8e8 100%)}

/* services */
.services{position:absolute;top:1146px;left:0;width:1200px;height:631px}
.services h2{text-align:center;margin-top:88px;font-size:35px;font-weight:600}
.service-grid{position:absolute;left:85px;top:147px;width:1030px;display:grid;grid-template-columns:repeat(3,1fr)}
.service-grid div{height:100px;display:flex;align-items:center;justify-content:center;text-align:center;color:var(--brick);font-size:17px;font-weight:500;line-height:25px;border-top:1px solid var(--line);padding:0 20px}
.service-grid div:nth-child(3n+2){border-left:1px solid var(--line);border-right:1px solid var(--line)}

/* extended */
.extended{position:absolute;top:1777px;left:0;width:1200px;height:557px;background:linear-gradient(100deg,#3d6762 0%,#56807a 45%,#4c7570 100%)}
.extended h2{position:absolute;left:85px;top:149px;font-size:49px;line-height:55px;color:#fff;font-weight:700;width:520px}
.action{position:absolute;left:686px;width:463px;height:77px;display:flex;align-items:center;padding:0 24px;gap:18px;color:#fff;font-size:17px;font-weight:500}
.action.brick{background:var(--brick)}
.action.mint{background:var(--mint)}
.action span{flex:1}

/* testimonial */
.testimonial{position:absolute;top:2334px;left:0;width:1200px;height:570px;background:linear-gradient(90deg,#f4f4f4,#ececec)}
.portrait{position:absolute;left:93px;top:48px;width:449px;height:522px;background:linear-gradient(180deg,#d6d8d8,#b9bcbd)}
.testimonial h3{position:absolute;left:622px;top:110px;width:430px;font-size:38px;line-height:47px;font-weight:600}
.testimonial p{position:absolute;left:622px;top:271px;width:430px;font-size:14.5px;line-height:27.5px;color:var(--body)}
.testimonial .author{top:423px;color:var(--teal);font-size:15px;line-height:24px}

/* cta */
.cta{position:absolute;top:2904px;left:0;width:1200px;height:468px;text-align:center}
.cta h2{position:relative;z-index:2;margin-top:110px;font-size:35px;line-height:42px;font-weight:600}
.cta p{position:relative;z-index:2;width:520px;margin:18px auto 0;font-size:14.5px;line-height:27px;color:var(--body)}

/* footer */
.site-footer{position:absolute;top:3477px;left:0;width:1200px;height:514px;background:var(--footer);color:#fff}
.fcol{position:absolute;top:97px;font-size:14px;line-height:26.5px}
.fcol .label{color:var(--footer-label)}
.fcol b{font-weight:500}
.flinks{position:absolute;top:97px;font-size:14px;line-height:26.5px;color:var(--footer-label)}
.legal{position:absolute;left:99px;top:337px;font-size:10.5px;line-height:16px;color:#a8a8aa}
.social{position:absolute;left:1018px;top:348px;display:flex;gap:16px}
.social i{width:14px;height:14px;border-radius:50%;background:#fff;display:block}
</style>
</head>
<body>

<header class="site-header">
  <a class="brand abs" href="#"><span class="mark"></span>LMT Vexa</a>
  <nav class="main-nav abs">
    <a href="#">PAY NOW</a><a href="#">FOR CONSUMERS</a><a href="#">CONTACT US</a><a href="#">ABOUT US</a><a href="#">LV BLOG</a>
  </nav>
  <div class="search abs"><svg width="12" height="12" viewBox="0 0 12 12"><circle cx="5" cy="5" r="3.8" fill="none" stroke="#222" stroke-width="1.5"/><line x1="8" y1="8" x2="11" y2="11" stroke="#222" stroke-width="1.5"/></svg>Search</div>
  <a class="client-login abs" href="#">CLIENT LOGIN</a>
</header>

<nav class="tab-bar" style="top:76px">
  <a class="tab brick" href="#">Healthcare AR<br>Management<svg width="18" height="34" viewBox="0 0 18 34"><polyline points="2,2 16,17 2,32" fill="none" stroke="#fff" stroke-width="2"/></svg></a>
  <a class="tab teal" href="#">Commercial AR<br>Management<svg width="18" height="34" viewBox="0 0 18 34"><polyline points="2,2 16,17 2,32" fill="none" stroke="#fff" stroke-width="2"/></svg></a>
  <a class="tab mint" style="background:linear-gradient(90deg,#2f5f58,#6aa894)" href="#">Insurance Over<br>payment Recovery<svg width="18" height="34" viewBox="0 0 18 34"><polyline points="2,2 16,17 2,32" fill="none" stroke="#fff" stroke-width="2"/></svg></a>
</nav>

<section class="hero" role="img" aria-label="Photo of a team of women working together at an office desk">
  <h1>Proven Results<br>in Debt Collection</h1>
  <p>Extended Business Office Services and Business Debt Collection for Healthcare and Commercial AR Management</p>
  <a class="btn" href="#">OUR STRATEGY</a>
</section>

<section class="welcome">
  <h2>Welcome</h2>
  <p>Whether you need help establishing an internal recovery system or providing business debt collection to clients for the reimbursement of services, LMT Vexa has the expertise to institute the right program for your needs.</p>
  <a class="btn" href="#">ABOUT US</a>
  <div class="skyline" role="img" aria-label="Faint line illustration of a city skyline"></div>
</section>

<section class="services">
  <h2>Customizable Services</h2>
  <div class="service-grid">
    <div>AR Receivables Management -<br>Primary and Secondary</div>
    <div>Self-Pay AR Management</div>
    <div>Urgent Care Specialist<br>AR Management</div>
    <div>Letter/Statement Service</div>
    <div>Specialist Financial Counselors -<br>CPAR certified</div>
    <div>Early Out-Pre Business<br>Debt Collections</div>
    <div>IVR and Online Payment<br>Processing</div>
    <div>Call Center</div>
    <div>Bad Business Debt Collection</div>
    <div></div>
    <div>Third Party Billing Solutions</div>
    <div></div>
  </div>
</section>

<section class="extended" role="img" aria-label="Photo of a smiling man working at a desk, tinted teal">
  <h2>Extended Business Office and Business Debt Collection Services</h2>
  <a class="action brick" style="top:105px" href="#">
    <svg width="34" height="28" viewBox="0 0 34 28"><rect x="2" y="5" width="30" height="18" fill="none" stroke="#fff" stroke-width="1.6"/><circle cx="17" cy="14" r="5" fill="none" stroke="#fff" stroke-width="1.6"/></svg>
    <span>Report a Payment Now</span>
    <svg width="22" height="14" viewBox="0 0 22 14"><path d="M1 7h19M14 1l6 6-6 6" fill="none" stroke="#fff" stroke-width="1.6"/></svg></a>
  <a class="action mint" style="top:195px" href="#">
    <svg width="34" height="34" viewBox="0 0 34 34"><rect x="6" y="3" width="22" height="28" fill="none" stroke="#fff" stroke-width="1.6"/><path d="M11 11h12M11 17h12M11 23h8" stroke="#fff" stroke-width="1.6"/></svg>
    <span>Request Account Documentation</span>
    <svg width="22" height="14" viewBox="0 0 22 14"><path d="M1 7h19M14 1l6 6-6 6" fill="none" stroke="#fff" stroke-width="1.6"/></svg></a>
  <a class="action mint" style="top:285px" href="#">
    <svg width="34" height="34" viewBox="0 0 34 34"><circle cx="17" cy="17" r="13" fill="none" stroke="#fff" stroke-width="1.6"/><circle cx="11" cy="17" r="1.6" fill="#fff"/><circle cx="17" cy="17" r="1.6" fill="#fff"/><circle cx="23" cy="17" r="1.6" fill="#fff"/></svg>
    <span>LMT Vexa Contacted The Wrong Person</span>
    <svg width="22" height="14" viewBox="0 0 22 14"><path d="M1 7h19M14 1l6 6-6 6" fill="none" stroke="#fff" stroke-width="1.6"/></svg></a>
  <a class="action mint" style="top:375px" href="#">
    <svg width="34" height="34" viewBox="0 0 34 34"><circle cx="10" cy="10" r="7" fill="none" stroke="#fff" stroke-width="1.6"/><line x1="5" y1="15" x2="15" y2="5" stroke="#fff" stroke-width="1.6"/><path d="M18 32V16a2 2 0 0 1 4 0v8h6a3 3 0 0 1 3 3v5" fill="none" stroke="#fff" stroke-width="1.6"/></svg>
    <span>Dispute an Account or Claim</span>
    <svg width="22" height="14" viewBox="0 0 22 14"><path d="M1 7h19M14 1l6 6-6 6" fill="none" stroke="#fff" stroke-width="1.6"/></svg></a>
</section>

<section class="testimonial">
  <div class="portrait" role="img" aria-label="Photo of a smiling man in a grey t-shirt"></div>
  <h3>“I could not be happier with the work LMT Vexa”</h3>
  <p>“I could not be happier with the work LMT Vexa performs for us as our EBO / Outside Collection Agency. We have had several EBOs / Outside Collection Agencies and without a doubt, LMT Vexa has outperformed them all! I highly recommend LMT Vexa and am glad to have them as partner.”</p>
  <p class="author">Dana Whitfield, EBD, Employer Services<br>Collections Manager</p>
</section>

<section class="cta">
  <h2>Reduce overhead and improve<br>operational efficiency now</h2>
  <p>Because each person has unique needs and abilities, we work with you to build the perfect system for your situation. Let’s talk!</p>
  <a class="btn" href="#">GET STARTED</a>
  <div class="skyline" role="img" aria-label="Faint line illustration of a city skyline"></div>
</section>

<nav class="tab-bar" style="top:3372px">
  <a class="tab brick" href="#">Healthcare AR<br>Management<svg width="18" height="34" viewBox="0 0 18 34"><polyline points="2,2 16,17 2,32" fill="none" stroke="#fff" stroke-width="2"/></svg></a>
  <a class="tab teal" href="#">Commercial AR<br>Management<svg width="18" height="34" viewBox="0 0 18 34"><polyline points="2,2 16,17 2,32" fill="none" stroke="#fff" stroke-width="2"/></svg></a>
  <a class="tab mint" href="#">Insurance Over<br>payment Recovery<svg width="18" height="34" viewBox="0 0 18 34"><polyline points="2,2 16,17 2,32" fill="none" stroke="#fff" stroke-width="2"/></svg></a>
</nav>

<footer class="site-footer">
  <div class="fcol" style="left:99px">
    <div class="label">Address</div><b>P.O.B. 2140, Marietta, GA 30061</b>
    <div class="label">Phone</div><b>470-555-0142</b>
    <div class="label">Fax</div><b>770-555-0187</b>
  </div>
  <div class="fcol" style="left:375px">
    <div class="label">Fax</div><b>770-555-0187</b>
    <div class="label">Email</div><b>contact@lmtvexa.net</b><br>
    <b>To consent to text messaging: text<br>CONTACT to 833-555-0126</b>
  </div>
  <div class="flinks" style="left:836px">Contact Us<br>About Us<br>LV Blog<br>Client Login<br>Pay Now</div>
  <div class="flinks" style="left:946px">Careers<br>Resources<br>Subscribe Newsletter</div>
  <div class="legal">
    Privacy Policy &nbsp;|&nbsp; Terms of Use<br>
    All Materials © 2021 LMT Vexa Corporation<br>
    This communication is from a debt collector and an attempt to collect a debt; any information obtained will be used for that purpose.<br>
    LMT Vexa Corporation takes all Federal and State Laws very seriously. We follow the Fair Debt Collection Practice Act (FDCPA) and are HIPAA compliant.<br><br>
    LMT Vexa Corporation - NMLS No. 1000417
  </div>
  <div class="social"><i></i><i></i><i></i></div>
</footer>

</body>
</html>
```